Chicago Property Management Flyer

We need a brochure/flyer to market our property management services to Chicago property owners. I believe that my preference is single page, double sided, but a bi-fold or tri-fold format may also work. I have provided our logo, and some example images in case that is helpful. Refer to our website at http://www.velmorehq.net/ for more info.

Industry/Entity Type

Property Management

Font styles to use
Sans Serif

```html
<!DOCTYPE html>
<html lang="en">
<head>
<meta charset="utf-8">
<title>Velmore Property Management – Owner Services Brochure</title>
<link rel="stylesheet" href="https://fonts.googleapis.com/css2?family=Open+Sans:wght@400&family=Roboto+Condensed:wght@700&family=Arimo:wght@400&family=Montserrat:wght@600&display=swap">
<style>
  :root{
    --blue-deep:#0b2a78;
    --blue-mid:#1b4fb0;
    --blue-light:#3a72c8;
    --lime:#8ee51c;
    --white:#ffffff;
    --gray-dark:#2a2c30;
    --gray-mid:#6d7078;
    --gray-light:#b9bcc2;
  }
  *{margin:0;padding:0;box-sizing:border-box}
  html,body{width:1200px;height:834px;overflow:hidden;background:var(--white)}
  .brochure{position:relative;width:1200px;height:834px;overflow:hidden;font-family:"Open Sans",sans-serif;color:var(--white)}
  .city-backdrop{position:absolute;inset:0;background:
    radial-gradient(ellipse at 70% 20%, #2a5fc0 0%, transparent 55%),
    linear-gradient(180deg,#1846a6 0%,#123c98 45%,#0c2d7e 100%)}
  .graphics{position:absolute;inset:0}
  .fold{position:absolute;top:0;bottom:0;width:1px;background:rgba(0,0,0,.35)}
  .feature{position:absolute;width:292px}
  .feature h2{font-family:"Roboto Condensed",sans-serif;font-weight:700;font-size:14px;color:var(--lime);line-height:18px;letter-spacing:-.1px}
  .feature p{font-size:12.6px;line-height:22.2px;text-align:justify;text-align-last:left}
  .feature-icon{position:absolute;width:34px;height:38px}
  .photo-spot{position:absolute;border-radius:50%;border:2px dashed var(--white)}
  .contact{position:absolute;left:850px;font-family:"Arimo",sans-serif;font-size:24px;display:flex;align-items:center;gap:12px;white-space:nowrap}
  .contact svg{flex:none}
  .brand{position:absolute;left:100px;top:686px;width:200px;text-align:center;font-family:"Montserrat",sans-serif;font-weight:600;color:var(--white)}
  .brand-mark{width:34px;height:34px;border:3px solid var(--white);margin:0 auto 36px}
  .brand-name{font-size:15.5px;letter-spacing:.2px;line-height:18px}
  .brand-sub{font-size:11px;letter-spacing:3px;line-height:14px}
</style>
</head>
<body>
<main class="brochure">
  <div class="city-backdrop" role="img" aria-label="Aerial view of the Chicago skyline tinted deep blue"></div>

  <svg class="graphics" width="1200" height="834" viewBox="0 0 1200 834">
    <defs>
      <linearGradient id="grayCity" x1="0" y1="0" x2="1" y2="1">
        <stop offset="0" stop-color="#8d9097"/>
        <stop offset=".5" stop-color="#55585f"/>
        <stop offset="1" stop-color="#1f2125"/>
      </linearGradient>
    </defs>
    <polygon points="400,545 1200,290 1200,834 400,834" fill="url(#grayCity)" role="img" aria-label="Black and white aerial photo of downtown Chicago towers"/>
    <polygon points="400,533 1200,278 1200,300 400,548" fill="var(--lime)"/>
  </svg>

  <div class="fold" style="left:400px"></div>
  <div class="fold" style="left:798px"></div>

  <!-- Left panel -->
  <svg class="feature-icon" style="left:30px;top:84px" viewBox="0 0 34 38"><polygon points="17,0 34,9.5 34,28.5 17,38 0,28.5 0,9.5" fill="var(--lime)"/><circle cx="17" cy="17" r="6" fill="none" stroke="#fff" stroke-width="2"/><path d="M9 27h16" stroke="#fff" stroke-width="2"/></svg>
  <section class="feature" style="left:80px;top:52px">
    <h2>Save Time and Headaches</h2>
    <p>We have a team in place to tackle all aspects of property management for you. Never worry about leasing, tenants, maintenance, regulations, etc.</p>
  </section>

  <svg class="feature-icon" style="left:30px;top:192px" viewBox="0 0 34 38"><polygon points="17,0 34,9.5 34,28.5 17,38 0,28.5 0,9.5" fill="var(--lime)"/><path d="M8 19l9-8 9 8M11 18v9h12v-9" fill="none" stroke="#fff" stroke-width="2"/></svg>
  <section class="feature" style="left:80px;top:175px">
    <h2>Maximize Your Investment Assets</h2>
    <p>Your properties are expensive assets with lots of potential. Put the right professionals in place to protect, maintain, and maximize their value.</p>
  </section>

  <svg class="feature-icon" style="left:30px;top:310px" viewBox="0 0 34 38"><polygon points="17,0 34,9.5 34,28.5 17,38 0,28.5 0,9.5" fill="var(--lime)"/><rect x="9" y="13" width="16" height="10" rx="2" fill="none" stroke="#fff" stroke-width="2"/><circle cx="17" cy="18" r="2" fill="#fff"/></svg>
  <section class="feature" style="left:80px;top:275px">
    <h2>Increase Income</h2>
    <p>With our experience and market knowledge we can establish optimal rent prices, lease apartments quickly, reduce turnover, and navigate complex housing agency processes to ensure maximum income to you.</p>
  </section>

  <svg class="feature-icon" style="left:30px;top:441px" viewBox="0 0 34 38"><polygon points="17,0 34,9.5 34,28.5 17,38 0,28.5 0,9.5" fill="var(--lime)"/><circle cx="12" cy="14" r="3" fill="none" stroke="#fff" stroke-width="2"/><circle cx="22" cy="14" r="3" fill="none" stroke="#fff" stroke-width="2"/><path d="M8 26c0-4 8-4 8 0M18 26c0-4 8-4 8 0" fill="none" stroke="#fff" stroke-width="2"/></svg>
  <section class="feature" style="left:80px;top:419px">
    <h2>Reduce Expenses, Maximize Profits</h2>
    <p>Maximize your profits by benefitting from our economies of scale, systems and processes, specialized knowledge, industry network, and buying power</p>
  </section>

  <div class="photo-spot" style="left:129px;top:529px;width:138px;height:138px;background:linear-gradient(180deg,#b7d4ee 0%,#a2533c 45%,#8a3e2c 75%,#5f8a3c 100%)" role="img" aria-label="Red brick Chicago courtyard apartment building"></div>

  <div class="brand">
    <div class="brand-mark"></div>
    <div class="brand-name">VELMORE PROPERTY</div>
    <div class="brand-sub">MANAGEMENT</div>
  </div>

  <!-- Middle panel -->
  <svg class="feature-icon" style="left:418px;top:99px" viewBox="0 0 34 38"><polygon points="17,0 34,9.5 34,28.5 17,38 0,28.5 0,9.5" fill="var(--lime)"/><circle cx="17" cy="19" r="8" fill="none" stroke="#fff" stroke-width="2"/><path d="M17 17v6" stroke="#fff" stroke-width="2"/><circle cx="17" cy="14" r="1.3" fill="#fff"/></svg>
  <section class="feature" style="left:472px;top:52px">
    <h2>Stay Informed</h2>
    <p>With access to all of your property information, documentation, and financials through your online portal of our property management system you and your accountant can stay informed as needed</p>
  </section>

  <svg class="feature-icon" style="left:418px;top:211px" viewBox="0 0 34 38"><polygon points="17,0 34,9.5 34,28.5 17,38 0,28.5 0,9.5" fill="var(--lime)"/><rect x="9" y="12" width="16" height="14" fill="none" stroke="#fff" stroke-width="2"/><path d="M13 23v-3M17 23v-5M21 23v-7" stroke="#fff" stroke-width="2"/></svg>
  <section class="feature" style="left:472px;top:197px">
    <h2>Grow Your Investment Portfolio</h2>
    <p>With our management team focused on profitably managing your existing properties, we can then help you expand to future investments</p>
  </section>

  <div class="photo-spot" style="left:514px;top:315px;width:138px;height:138px;background:linear-gradient(180deg,#9cc4ea 0%,#d2b98a 40%,#b89d6e 75%,#4f7a34 100%)" role="img" aria-label="Tan brick Chicago walk-up apartment building"></div>

  <!-- Right panel -->
  <div class="contact" style="top:66px;left:898px">
    <svg width="26" height="26" viewBox="0 0 26 26"><circle cx="13" cy="13" r="11" fill="none" stroke="var(--lime)" stroke-width="2.5"/><path d="M9 8c0 6 3 9 9 10l1-3-3-1-1 1c-2-1-3-2-4-4l1-1-1-3z" fill="var(--lime)"/></svg>
    <span>773-555-0148</span>
  </div>
  <div class="contact" style="top:106px">
    <svg width="28" height="28" viewBox="0 0 28 28" fill="none" stroke="var(--lime)" stroke-width="2"><circle cx="14" cy="14" r="11"/><ellipse cx="14" cy="14" rx="5" ry="11"/><path d="M3 14h22M5 8h18M5 20h18"/></svg>
    <span>www.velmorehq.net</span>
  </div>
  <div class="contact" style="top:145px;left:838px">
    <svg width="28" height="26" viewBox="0 0 28 26"><path d="M2 10l12-8 12 8v14H2z" fill="var(--lime)"/><path d="M2 10l12 8 12-8" fill="none" stroke="#fff" stroke-width="1.6"/></svg>
    <span>owners@velmorehq.net</span>
  </div>
</main>
</body>
</html>
```